Edible Insect Sticker packaging design

The successful designer for this product will be hired again for more packaging design products in this product range.
We are a company that manufactures edible insects and we have some new products coming out we ned packaging for. As you can imagine the stickers are very small 50mm x 50mm.
Each sticker design will be in a set  of 2 (one for the front and one for the back of the packaging).
The front will contain the weight of the product (in grams) as well as the name of the product and design.
The back will contain our company logo and info as well as NIP (Nutritional Information Panel), ingredient declaration, and 3-4 lines of information about how edible insects are great for the environment.
At this stage I would like the packaging to have a slightly environmental free, but still colourful and eye catching. I am open to any suggestions for the design though if you have some great ideas!
Must also contain the slogan (on front or back), "Are you Brave Enough?"
There are several products in the range, and would like the labels to be in a set. Basic lay out will be the same for each product, and the front sticker will be slightly different.
Products are
Zib-A-Lop Tundle- a fly shaped chocolate that contains coconut and fly pupae
Plinky Pebbles- 5 x roasted crickets
Tootle Twirlies- 5 x roasted mealworms
Fudge Dipped Fidgets- 5 x insects, chocolate coated in milk, white or dark chocolate. Insects include crickets, mealworms and fly pupae
Specific information (eg, NIP, ingredients etc) will be sent to chosen designer to add to the deisgn.
Attached is image of 3 products (Zib-A-Lop Tundle, roasted mealworms and roasted crickets) as well as logo. The chocolate coated bugs are the 2 types of roasted bugs pictured in the attachment coated in chocolate.

Updates
Design can be square or round 

Reason: Several designers have asked for an extension to submit new/ revised designs.

Reason: I have extended the deadline by one day to allow for revisions and new designs to be submitted.

```html
<!DOCTYPE html>
<html lang="en">
<head>
<meta charset="utf-8">
<title>Plinky Pebbles – Front Label</title>
<link rel="stylesheet" href="https://fonts.googleapis.com/css2?family=Titan+One&family=Oswald:wght@500;700&display=swap">
<style>
  :root {
    --stripe-light: #fdca7c;
    --stripe-dark: #f9bb6c;
    --band-brown: #a9632b;
    --band-edge: #7b421b;
    --panel-glow: #f8dcad;
    --panel-edge: #c7843f;
    --title-red: #e5392a;
    --shadow-brown: #8a4a1e;
    --ink-brown: #6b3a17;
    --banner-red: #e63a2c;
    --white: #ffffff;
  }
  html, body {
    margin: 0;
    padding: 0;
    width: 1200px;
    height: 1200px;
    overflow: hidden;
    background: var(--stripe-light);
  }
  .label {
    display: block;
    width: 1200px;
    height: 1200px;
  }
  .product-title {
    font-family: "Titan One", sans-serif;
    font-size: 176px;
    letter-spacing: 2px;
    fill: var(--title-red);
  }
  .count-callout {
    font-family: "Titan One", sans-serif;
    fill: var(--white);
    stroke: var(--shadow-brown);
    stroke-width: 6px;
    paint-order: stroke fill;
  }
  .count-big { font-size: 118px; }
  .count-small { font-size: 62px; }
  .net-weight {
    font-family: "Oswald", sans-serif;
    font-weight: 700;
    font-size: 120px;
    fill: var(--ink-brown);
  }
  .slogan {
    font-family: "Oswald", sans-serif;
    font-weight: 500;
    font-size: 58px;
    letter-spacing: 2px;
    fill: var(--white);
  }
</style>
</head>
<body>
<svg class="label" viewBox="0 0 1200 1200" xmlns="http://www.w3.org/2000/svg">
  <defs>
    <pattern id="stripes" width="1200" height="106" patternUnits="userSpaceOnUse">
      <rect width="1200" height="53" fill="var(--stripe-light)"/>
      <rect y="53" width="1200" height="53" fill="var(--stripe-dark)"/>
    </pattern>
    <radialGradient id="panelGlow" cx="50%" cy="48%" r="60%">
      <stop offset="0" stop-color="var(--panel-glow)"/>
      <stop offset="1" stop-color="var(--panel-edge)"/>
    </radialGradient>
    <linearGradient id="illustrationTone" x1="0" y1="0" x2="0" y2="1">
      <stop offset="0" stop-color="#b8895a" stop-opacity="0.35"/>
      <stop offset="1" stop-color="#8a5a30" stop-opacity="0.45"/>
    </linearGradient>
  </defs>

  <rect class="background" width="1200" height="1200" fill="url(#stripes)"/>

  <g class="center-band">
    <rect x="331" y="0" width="536" height="1200" fill="var(--band-brown)"/>
    <rect x="343" y="0" width="6" height="1200" fill="var(--band-edge)"/>
    <rect x="849" y="0" width="6" height="1200" fill="var(--band-edge)"/>
    <rect x="365" y="0" width="468" height="1200" fill="url(#panelGlow)"/>
  </g>

  <g class="hero-illustration" role="img" aria-label="Engraved-style drawing of a cricket, viewed from above">
    <ellipse cx="600" cy="760" rx="170" ry="330" fill="url(#illustrationTone)"/>
  </g>

  <g class="product-title">
    <text x="600" y="265" text-anchor="middle">Plinky</text>
    <text x="640" y="440" text-anchor="middle">Pebbles</text>
  </g>

  <g class="count-callout">
    <text class="count-big" x="95" y="835">5X</text>
    <text class="count-small" x="86" y="905">ROASTED</text>
    <text class="count-small" x="98" y="970">CRICKETS</text>
  </g>

  <text class="net-weight" x="1018" y="855" text-anchor="middle">30g</text>

  <g class="slogan-banner">
    <polygon points="0,1062 1200,1005 1200,1105 0,1162" fill="var(--banner-red)"/>
    <polygon points="150,1080 150,1126 188,1101" fill="var(--white)"/>
    <polygon points="1052,1055 1052,1101 1014,1080" fill="var(--white)"/>
    <text class="slogan" x="602" y="1106" text-anchor="middle" transform="rotate(-2.7 600 1085)">ARE YOU BRAVE ENOUGH?</text>
  </g>
</svg>
</body>
</html>
```